A5 Flyer for Window Cleaning Company

2 sided Flyer design required for window cleaning company. One side to include we use traditional and hot water fed pole window cleaning systems, conservatory cleaning, and fascia and soffit cleaning. The other side to be for Gutter cleaning. See the must haves section of project brief for more info. Mixture of some images and text for both sides. ( do not have to use all images supplied). The flyer will be used to promote the business to new residential customers.

Target Market(s)

Private households/new customers

Industry/Entity Type

Window Cleaning

Font styles to use
Serif

Requirements
Must have
• Company address ( 7 Old Pennick Court Harlow Street Edinburgh EH4 9RQ
Phone numbers( 0131 482 7719 0800 061 2287).
Website and email address ( info@falconbright-cleaning.example)
Excellent Customer Service. Competitive prices. Established 1994.
Side 1of flyer = Falconbright Window Cleaning Side 2 of flyer Falconbright Gutter Cleaning.
Nice to have
• Professional look.

```html
<!DOCTYPE html>
<html lang="en">
<head>
<meta charset="utf-8">
<title>Falconbright Cleaning – A5 Flyers</title>
<link href="https://fonts.googleapis.com/css2?family=Libre+Caslon+Text:wght@700&family=Roboto:ital,wght@0,400;0,700;1,700&display=swap" rel="stylesheet">
<style>
  :root{
    --page:#eaf3fc;
    --sky:#b3d4f2;
    --mid:#6fa3d9;
    --navy:#26215e;
    --ink:#1b1a2e;
    --icon:#2e5fb0;
    --grey:#e4e4e4;
    --white:#ffffff;
  }
  *{margin:0;padding:0;box-sizing:border-box}
  html,body{width:1200px;height:840px;overflow:hidden;background:var(--page)}
  body{position:relative;font-family:"Roboto",Arial,sans-serif;color:var(--ink)}
  .flyer{position:absolute;top:44px;width:531px;height:748px;background:var(--white);overflow:hidden;box-shadow:0 2px 8px rgba(40,60,100,.18)}
  .flyer--window{left:56px}
  .flyer--gutter{left:621px}
  .abs{position:absolute}
  .shapes{position:absolute;left:0;top:0}
  .brand{position:absolute;left:29px;top:27px;display:flex;align-items:center;gap:8px}
  .brand__mark{width:30px;height:30px;background:var(--mid)}
  .brand__name{font-weight:700;font-size:20px;color:var(--navy)}
  .title{position:absolute;left:24px;z-index:2;font-family:"Libre Caslon Text",Georgia,serif;font-weight:700;white-space:nowrap}
  .title--light{top:298px;font-size:31px;line-height:48px;color:var(--white);-webkit-text-stroke:1px var(--navy);text-shadow:2px 2px 0 var(--navy)}
  .title--dark{top:196px;font-size:31px;line-height:47px;color:var(--navy)}
  .services{position:absolute;left:24px;top:484px;font-weight:700;font-style:italic;font-size:21.5px;line-height:32.5px;color:var(--ink)}
  .contact-btn{position:absolute;left:181px;top:594px;width:169px;height:35px;border-radius:18px;background:var(--mid);color:var(--white);font-style:italic;font-weight:700;font-size:14px;display:flex;align-items:center;justify-content:center;gap:10px}
  .contact-btn svg{display:block}
  .footer{position:absolute;left:0;top:644px;width:531px;height:104px;background:var(--navy);color:var(--white)}
  .footer__col{position:absolute;top:20px;display:flex;gap:8px}
  .footer__col--addr{left:24px;font-size:12px;line-height:14.6px}
  .footer__col--phone{left:196px;font-size:14.5px;line-height:18px}
  .footer__col--mail{left:368px;font-size:12px;line-height:14.6px}
  .footer__rule{position:absolute;top:20px;width:1px;height:51px;background:rgba(255,255,255,.75)}
  .features{position:absolute;left:0;top:366px;width:531px;height:126px}
  .feature{position:absolute;top:22px;width:150px;text-align:center;font-weight:700;font-size:12px;line-height:14.5px;color:var(--ink)}
  .feature svg{display:block;margin:0 auto 8px}
  .gallery{position:absolute;left:0;top:492px;width:531px;height:152px;background:var(--grey)}
  .gallery__photo{position:absolute;top:10px;width:157px;height:133px;border-radius:6px}
</style>
</head>
<body>

<!-- Side 1: window cleaning -->
<section class="flyer flyer--window">
  <svg class="shapes" width="531" height="748" viewBox="0 0 531 748">
    <path d="M222 0 H531 V292 H180 Q140 292 148 252 Z" fill="var(--sky)"/>
    <path d="M0 271 H327 L222 458 Q215 470 200 470 H0 Z" fill="var(--mid)"/>
    <path d="M280 388 H349 L330 432 H261 Z" fill="var(--mid)"/>
    <path d="M478 457 H521 L511 485 H468 Z" fill="var(--sky)"/>
  </svg>
  <div class="abs" role="img" aria-label="Photo of a window cleaner in a blue cap and shirt washing a window with a squeegee" style="left:280px;top:18px;width:251px;height:274px;background:linear-gradient(160deg,#dfe7ee 0%,#7aa0c8 45%,#2d5f9e 100%)"></div>
  <div class="abs" role="img" aria-label="Satisfaction guarantee badge" style="left:163px;top:189px;width:86px;height:86px;border-radius:50%;background:var(--white)"><div style="margin:11px;width:64px;height:64px;border-radius:50%;background:#e0b23c"></div></div>
  <div class="brand"><span class="brand__mark"></span><span class="brand__name">Falconbright</span></div>
  <svg class="shapes" width="531" height="748" viewBox="0 0 531 748" role="img" aria-label="Photos of a gutter brush on a white gutter and a cleaned conservatory">
    <defs>
      <linearGradient id="gutterPhoto" x1="0" y1="0" x2="1" y2="1"><stop offset="0" stop-color="#eef0f2"/><stop offset="1" stop-color="#8c9aa6"/></linearGradient>
      <linearGradient id="consPhoto" x1="0" y1="0" x2="0" y2="1"><stop offset="0" stop-color="#c9d8e6"/><stop offset="0.55" stop-color="#a86a4e"/><stop offset="1" stop-color="#6f9a3e"/></linearGradient>
    </defs>
    <path d="M278 310 H377 L352 381 H256 Z" fill="url(#gutterPhoto)"/>
    <path d="M400 310 H531 V450 H356 Z" fill="url(#consPhoto)"/>
  </svg>
  <h1 class="title title--light">Falconbright<br>Window<br>Cleaning</h1>
  <p class="services">We use traditional and hot water fed pole<br>window cleaning systems, conservatory<br>cleaning, and fascia and soffit cleaning.</p>
  <div class="contact-btn">Contact Us
    <svg width="22" height="22" viewBox="0 0 22 22"><circle cx="11" cy="11" r="10" fill="var(--white)"/><path d="M11 5 V16 M6.5 11.5 L11 16 L15.5 11.5" fill="none" stroke="var(--mid)" stroke-width="2" stroke-linecap="round"/></svg>
  </div>
  <footer class="footer">
    <div class="footer__col footer__col--addr">
      <svg width="12" height="16" viewBox="0 0 12 16"><path d="M6 0 C2.7 0 0 2.6 0 5.8 C0 10 6 16 6 16 S12 10 12 5.8 C12 2.6 9.3 0 6 0 Z" fill="var(--mid)"/><circle cx="6" cy="5.8" r="2.2" fill="var(--navy)"/></svg>
      <address style="font-style:normal">7 Old Pennick Court<br>Harlow Street<br>Edinburgh EH4 9RQ</address>
    </div>
    <div class="footer__rule" style="left:181px"></div>
    <div class="footer__col footer__col--phone">
      <svg width="17" height="17" viewBox="0 0 24 24"><path d="M6.6 10.8 C8 13.6 10.4 16 13.2 17.4 L15.4 15.2 C15.7 14.9 16.1 14.8 16.4 15 C17.5 15.4 18.7 15.6 20 15.6 C20.6 15.6 21 16 21 16.6 V20 C21 20.6 20.6 21 20 21 C10.6 21 3 13.4 3 4 C3 3.4 3.4 3 4 3 H7.5 C8.1 3 8.5 3.4 8.5 4 C8.5 5.3 8.7 6.5 9.1 7.6 C9.2 7.9 9.1 8.3 8.9 8.6 Z" fill="var(--mid)"/></svg>
      <div>0131 482 7719<br>0800 061 2287</div>
    </div>
    <div class="footer__rule" style="left:350px"></div>
    <div class="footer__col footer__col--mail">
      <svg width="15" height="11" viewBox="0 0 15 11"><rect x="0.5" y="0.5" width="14" height="10" fill="none" stroke="var(--mid)"/><path d="M0.5 0.5 L7.5 6 L14.5 0.5" fill="none" stroke="var(--mid)"/></svg>
      <div>info@falconbright-<br>cleaning.example</div>
    </div>
  </footer>
</section>

<!-- Side 2: gutter cleaning -->
<section class="flyer flyer--gutter">
  <svg class="shapes" width="531" height="748" viewBox="0 0 531 748">
    <rect x="0" y="0" width="531" height="366" fill="var(--sky)"/>
    <path d="M0 0 H225 L180 140 Q170 166 140 166 H0 Z" fill="var(--white)"/>
    <path d="M309 366 L320 342 Q324 334 333 334 H381 L366 366 Z" fill="var(--mid)"/>
    <path d="M374 326 H411 L400 355 H366 Z" fill="var(--white)"/>
    <path d="M508 292 H531 V314 H500 Z" fill="var(--mid)"/>
  </svg>
  <svg class="shapes" width="531" height="748" viewBox="0 0 531 748" role="img" aria-label="Photo of a company van with a blue water-droplet livery parked outside a building">
    <defs><linearGradient id="vanPhoto" x1="0" y1="0" x2="0" y2="1"><stop offset="0" stop-color="#c4ccd4"/><stop offset="0.45" stop-color="#4fb0e8"/><stop offset="1" stop-color="#1f2a36"/></linearGradient></defs>
    <path d="M285 0 H531 V260 Q470 310 420 300 L290 250 Q262 238 262 200 Z" fill="url(#vanPhoto)"/>
  </svg>
  <div class="brand"><span class="brand__mark"></span><span class="brand__name">Falconbright</span></div>
  <h1 class="title title--dark">Falconbright<br>Gutter<br>Cleaning</h1>

  <div class="features">
    <div class="feature" style="left:25px">
      <svg width="40" height="44" viewBox="0 0 40 44" fill="none" stroke="var(--icon)" stroke-width="1.5"><circle cx="20" cy="18" r="15"/><circle cx="20" cy="18" r="10"/><path d="M20 12 L21.8 16 L26 16.4 L22.8 19.2 L23.8 23.4 L20 21.2 L16.2 23.4 L17.2 19.2 L14 16.4 L18.2 16 Z"/><path d="M11 30 L7 42 L12 39 L15 43 L18 33 M29 30 L33 42 L28 39 L25 43 L22 33"/></svg>
      Excellent<br>Customer Service
    </div>
    <div class="feature" style="left:190px">
      <svg width="44" height="44" viewBox="0 0 44 44" fill="none" stroke="var(--icon)" stroke-width="1.5"><circle cx="22" cy="22" r="16"/><circle cx="22" cy="22" r="11"/><path d="M25.5 16 Q24 14 22 14.5 Q19.5 15 19.5 18 V26 M17 21 H23.5 M17 27 H26.5 Q19.5 25 19.5 26"/><path d="M30 36 L36 42 M38 30 L30 38 L34 42"/></svg>
      Competitive<br>pricese
    </div>
    <div class="feature" style="left:354px">
      <svg width="44" height="44" viewBox="0 0 44 44" fill="none" stroke="var(--icon)" stroke-width="1.5"><path d="M8 6 Q20 0 32 6 V20 Q32 34 20 40 Q8 34 8 20 Z"/><path d="M12 9 Q20 5 28 9 V20 Q28 30 20 35 Q12 30 12 20 Z"/><path d="M14 20 L19 25 L27 15" stroke-width="2"/></svg>
      Established<br>1994
    </div>
  </div>

  <div class="gallery">
    <div class="gallery__photo" role="img" aria-label="Photo of a gloved hand clearing autumn leaves from a gutter" style="left:24px;background:linear-gradient(135deg,#d9dde0,#c58a3a 55%,#5a4a3c)"></div>
    <div class="gallery__photo" role="img" aria-label="Photo of a worker on a ladder cleaning a gutter against a blue sky" style="left:187px;background:linear-gradient(180deg,#3d8fe0,#6aa7e6 40%,#4a3a34 70%,#3a2c28)"></div>
    <div class="gallery__photo" role="img" aria-label="Labelled diagram of roofline parts: fascia, soffit, guttering, bargeboard, block end and down pipe" style="left:350px;background:linear-gradient(160deg,#ffffff 45%,#d6d6d6 60%,#9a6a52)"></div>
  </div>

  <footer class="footer">
    <div class="footer__col footer__col--addr">
      <svg width="12" height="16" viewBox="0 0 12 16"><path d="M6 0 C2.7 0 0 2.6 0 5.8 C0 10 6 16 6 16 S12 10 12 5.8 C12 2.6 9.3 0 6 0 Z" fill="var(--mid)"/><circle cx="6" cy="5.8" r="2.2" fill="var(--navy)"/></svg>
      <address style="font-style:normal">7 Old Pennick Court<br>Harlow Street<br>Edinburgh EH4 9RQ</address>
    </div>
    <div class="footer__rule" style="left:181px"></div>
    <div class="footer__col footer__col--phone">
      <svg width="17" height="17" viewBox="0 0 24 24"><path d="M6.6 10.8 C8 13.6 10.4 16 13.2 17.4 L15.4 15.2 C15.7 14.9 16.1 14.8 16.4 15 C17.5 15.4 18.7 15.6 20 15.6 C20.6 15.6 21 16 21 16.6 V20 C21 20.6 20.6 21 20 21 C10.6 21 3 13.4 3 4 C3 3.4 3.4 3 4 3 H7.5 C8.1 3 8.5 3.4 8.5 4 C8.5 5.3 8.7 6.5 9.1 7.6 C9.2 7.9 9.1 8.3 8.9 8.6 Z" fill="var(--mid)"/></svg>
      <div>0131 482 7719<br>0800 061 2287</div>
    </div>
    <div class="footer__rule" style="left:350px"></div>
    <div class="footer__col footer__col--mail">
      <svg width="15" height="11" viewBox="0 0 15 11"><rect x="0.5" y="0.5" width="14" height="10" fill="none" stroke="var(--mid)"/><path d="M0.5 0.5 L7.5 6 L14.5 0.5" fill="none" stroke="var(--mid)"/></svg>
      <div>info@falconbright-<br>cleaning.example</div>
    </div>
  </footer>
</section>

</body>
</html>
```